Spiritual journeyer, astrologer, Reiki master, underground music lover needs business card design

Initially I need a business card design (and possibly a logo for my new website). I offer astrological and energetic inquiry and guidance to clients in support of their life's evolutionary path. I combine an eclectic mix of methods with a focus on the mind body connection. I am a spiritual journeyer, astrologer, Reiki Master, certified personal trainer, soon to be black belt in Taekwondo (karate), and researcher into the benefits of music/sound vibrational therapy. And underground music lover :) The attached drawing is just something I drew freehand, it is symbolic of many things important to me. I wanted the figure to clearly be female. Her arms are open to catch the sky, the name of my new business is Noraweaver, and Nora is my daughter's name. This was just an idea I had, I'm open to suggestions. The photo is me with the planets in the sky as they were at the moment I was born (some years ago-LOL)

I have picked a final design. Thank you everyone for your time and effort.

Target Market(s)

Worldwide, what I do can be done in person or anywhere in the world via Skype

Industry/Entity Type

Professional Service

Contact Information for Business Card

Simple, unusual image with my business name and contact info

Font styles to use
Sans Serif

Requirements
Must have
• My website very clean, simple. Somehow combine biz name of Noraweaver with female figure catching/holding the starry sky? See my poor drawing I attached.
Nice to have
• Something that conveys all the unique, unusual, eclectic skills and capacities I have
Should not have
• Frilly, fancy, stuffy

```html
<!DOCTYPE html>
<html lang="en">
<head>
<meta charset="UTF-8">
<title>Noraweaver Business Card</title>
<link rel="stylesheet" href="https://fonts.googleapis.com/css2?family=Jost:wght@400&family=Karla:wght@400&family=Lora:ital@1&display=swap">
<style>
  :root {
    --page-bg: #e9e8ec;
    --card-bg: #ffffff;
    --brand-indigo: #2b1a6e;
    --name-orange: #e07a1f;
    --body-ink: #1e1e1e;
    --mark-grey: #d6d6d6;
  }
  * { margin: 0; padding: 0; box-sizing: border-box; }
  html, body {
    width: 1200px;
    height: 1200px;
    overflow: hidden;
    background: var(--page-bg);
  }
  .canvas {
    position: relative;
    width: 1200px;
    height: 1200px;
  }
  .business-card {
    position: absolute;
    left: 100px;
    top: 314px;
    width: 1000px;
    height: 572px;
    background: var(--card-bg);
    box-shadow: 0 12px 30px rgba(0, 0, 0, 0.18);
    overflow: hidden;
  }
  .logo-area {
    position: absolute;
    left: 318px;
    top: 118px;
    width: 344px;
    height: 344px;
  }
  .brand-name {
    position: absolute;
    left: 62px;
    top: 46px;
    font-family: "Jost", sans-serif;
    font-weight: 400;
    font-size: 58px;
    letter-spacing: 0.62em;
    color: var(--brand-indigo);
    text-transform: uppercase;
    white-space: nowrap;
  }
  .person-name {
    position: absolute;
    left: 96px;
    top: 218px;
    font-family: "Lora", serif;
    font-style: italic;
    font-size: 33px;
    color: var(--name-orange);
  }
  .service-line {
    position: absolute;
    left: 106px;
    top: 298px;
    font-family: "Karla", sans-serif;
    font-size: 25px;
    line-height: 1.35;
    color: var(--body-ink);
  }
  .contact-list {
    position: absolute;
    left: 120px;
    top: 424px;
    list-style: none;
    font-family: "Karla", sans-serif;
    font-size: 25px;
    line-height: 1.4;
    color: var(--body-ink);
  }
</style>
</head>
<body>
  <main class="canvas">
    <section class="business-card">
      <svg class="logo-area" viewBox="0 0 344 344" role="img" aria-label="Logo mark area: a female figure with open arms inside a star and circle">
        <circle cx="172" cy="172" r="170" fill="var(--mark-grey)" opacity="0.55"/>
      </svg>
      <h1 class="brand-name">Noraweaver</h1>
      <p class="person-name">Miriam Calloway</p>
      <p class="service-line">Astrological and Energetic<br>Guidance Inquiry</p>
      <ul class="contact-list">
        <li>www.noraweaver.com</li>
        <li>email@noraweaver.com</li>
        <li>555-014-2739</li>
      </ul>
    </section>
  </main>
</body>
</html>
```